Stationary for Vornik Consulting

Hi

I am after stationary designs for my company - Vornik Consulting. I have a logo - recently designed by PixelHarbor. Vornik ( sales spelt backwards ) is a sales consultancy - including sales training, sales coaching and business management.

I have attached some of the artwork I already have, as well as a few ideas
1. Use supplied logo's
2. back of business card to use the logo with the dark background and white text
3. details to be included on card are
Logo
Delmo Kastrani
p: +61491570156
e: delmo@vornikconsulting.com.au
w: www.vornikconsulting.com.au
PO Box 417, Kelridge Heights, Tasmania, 7209

4. I am after designs for business cards, A4 letterhead and A5 letterhead

Thanks in Advance

Delmo

```html
<!DOCTYPE html>
<html lang="en">
<head>
<meta charset="utf-8">
<title>Vornik Consulting Stationery</title>
<link href="https://fonts.googleapis.com/css2?family=Open+Sans:wght@400;600;700&display=swap" rel="stylesheet">
<style>
:root{
  --navy:#2f4350;
  --orange:#e04b25;
  --paper:#ffffff;
  --ground:#ebecee;
  --ink:#3a3f44;
  --muted:#7b8288;
  --rule:#c9ced2;
}
*{box-sizing:border-box;margin:0;padding:0}
html,body{width:1200px;height:795px;overflow:hidden}
body{background:var(--ground);font-family:"Open Sans",Arial,sans-serif;color:var(--ink);position:relative}
.sheet{position:absolute;background:var(--paper);box-shadow:0 3px 10px rgba(0,0,0,.14);overflow:hidden}
.band{position:absolute;background:var(--navy)}
.accent{position:absolute;background:var(--orange)}
.brand{position:absolute;display:flex;align-items:center;gap:6px;font-weight:700;color:var(--navy);white-space:nowrap;letter-spacing:.2px;line-height:1}
.brand::before{content:"";width:.7em;height:.7em;background:var(--orange);flex:none}

/* letterheads */
.letterhead.a4{left:40px;top:36px;width:370px;height:523px}
.letterhead.a5{left:440px;top:36px;width:330px;height:467px}
.letterhead .brand{left:28px;top:32px;font-size:15px}
.letterhead.a5 .brand{left:24px;top:30px;font-size:12px}
.contact-head{position:absolute;right:22px;top:26px;text-align:right;font-size:5.6px;line-height:1.55;color:var(--navy);white-space:nowrap}
.head-rule{position:absolute;left:28px;right:22px;top:58px;height:1px;background:var(--rule)}
.letterhead.a5 .head-rule{left:24px}
.head-rule::after{content:"";position:absolute;right:0;top:0;width:35%;height:1px;background:var(--orange)}
.letter-body{position:absolute;left:28px;right:30px;top:78px;font-size:6px;line-height:1.55}
.letterhead.a5 .letter-body{left:24px;right:24px;top:74px;font-size:5.4px}
.letter-body p{margin-bottom:7px}
.letter-body .addressee b{font-weight:700}
.letter-body .closing{margin-top:12px}
.letterhead .band.foot{left:0;right:0;bottom:0;height:34px}
.letterhead .accent.foot{left:0;right:0;bottom:38px;height:3px}
.letterhead.a5 .band.foot{height:30px}
.letterhead.a5 .accent.foot{bottom:34px}

/* envelope */
.envelope{left:800px;top:36px;width:360px;height:180px}
.envelope .band.top{left:0;right:0;top:0;height:30px}
.envelope .accent.top{left:0;width:120px;top:34px;height:3px}
.envelope .brand{left:30px;top:72px;font-size:13px}

/* compliment slip */
.compliment{left:800px;top:236px;width:360px;height:210px}
.compliment .band.side{left:0;top:0;bottom:0;width:70px}
.compliment .accent.side{left:74px;top:0;bottom:0;width:3px}
.compliment .brand{left:118px;top:62px;font-size:15px}
.compliment .details{left:118px;top:88px}

/* cards */
.card{width:210px;height:120px}
.card.details-side{left:40px;top:610px}
.card.details-side .band.side{right:0;top:0;bottom:0;width:22px}
.card.details-side .accent.side{right:26px;top:0;bottom:0;width:3px}
.card.details-side .brand{left:18px;top:20px;font-size:11px}
.person{position:absolute;left:18px;top:42px;font-size:9px;font-weight:700;color:var(--orange);white-space:nowrap}
.person span{font-weight:400;color:var(--muted);font-size:6.5px}
.card.details-side .details{left:18px;top:62px}
.card.logo-side{left:280px;top:610px}
.card.logo-side .band.foot{left:0;right:0;bottom:0;height:22px}
.card.logo-side .accent.foot{left:0;right:0;bottom:26px;height:3px}
.card.logo-side .brand{left:38px;top:38px;font-size:14px}

.details{position:absolute;list-style:none;font-size:6px;line-height:1.9;color:var(--navy);white-space:nowrap}
.details li{display:flex;align-items:center;gap:4px}
.details svg{width:6px;height:6px;fill:var(--navy);flex:none}
</style>
</head>
<body>

<section class="sheet letterhead a4">
  <div class="brand">Vornik Consulting</div>
  <div class="contact-head">www.vornikconsulting.com.au | delmo@vornikconsulting.com.au<br>PO Box 417, Kelridge Heights, Tasmania, 7209</div>
  <div class="head-rule"></div>
  <div class="letter-body">
    <p class="addressee">To<br><b>Mr. Tavin Rell</b><br>Executive Graphic Designer<br>Harlow Company</p>
    <p>We help growing firms build sales teams that close with confidence. Our programs blend practical training, steady coaching and clear business management so every member of your team knows the next step and takes it.</p>
    <p>Each engagement starts with a short review of your current pipeline, your people and your targets. From there we shape a plan that fits your market, your budget and the pace your business needs.</p>
    <p>We would welcome the chance to talk about your goals. Please reach out at any time and we will arrange a meeting that suits you.</p>
    <p class="closing">Thanks and Regards,</p>
  </div>
  <div class="accent foot"></div>
  <div class="band foot"></div>
</section>

<section class="sheet letterhead a5">
  <div class="brand">Vornik Consulting</div>
  <div class="contact-head">www.vornikconsulting.com.au<br>delmo@vornikconsulting.com.au<br>PO Box 417, Kelridge Heights, Tasmania, 7209</div>
  <div class="head-rule"></div>
  <div class="letter-body">
    <p class="addressee">To<br><b>Mr. Tavin Rell</b><br>Executive Graphic Designer<br>Harlow Company</p>
    <p>We help growing firms build sales teams that close with confidence. Our programs blend practical training, steady coaching and clear business management so every member of your team knows the next step and takes it.</p>
    <p>Each engagement starts with a short review of your current pipeline, your people and your targets. From there we shape a plan that fits your market, your budget and the pace your business needs.</p>
    <p>We would welcome the chance to talk about your goals. Please reach out at any time and we will arrange a meeting that suits you.</p>
    <p class="closing">Thanks and Regards,</p>
  </div>
  <div class="accent foot"></div>
  <div class="band foot"></div>
</section>

<section class="sheet envelope">
  <div class="band top"></div>
  <div class="accent top"></div>
  <div class="brand">Vornik Consulting</div>
</section>

<section class="sheet compliment">
  <div class="band side"></div>
  <div class="accent side"></div>
  <div class="brand">Vornik Consulting</div>
  <ul class="details">
    <li><svg viewBox="0 0 10 10"><rect x="1" y="2" width="8" height="6"/></svg>delmo@vornikconsulting.com.au</li>
    <li><svg viewBox="0 0 10 10"><circle cx="5" cy="5" r="4"/></svg>www.vornikconsulting.com.au</li>
    <li><svg viewBox="0 0 10 10"><path d="M5 0a3.5 3.5 0 0 1 3.5 3.5C8.5 6 5 10 5 10S1.5 6 1.5 3.5A3.5 3.5 0 0 1 5 0z"/></svg>PO Box 417, Kelridge Heights, Tasmania, 7209</li>
  </ul>
</section>

<section class="sheet card details-side">
  <div class="accent side"></div>
  <div class="band side"></div>
  <div class="brand">Vornik Consulting</div>
  <div class="person">Delmo Kastrani <span>| Director</span></div>
  <ul class="details">
    <li><svg viewBox="0 0 10 10"><path d="M2 1h2l1 2.5-1.3 1a6 6 0 0 0 2.8 2.8l1-1.3L10 7v2c0 .6-.4 1-1 1A9 9 0 0 1 0 2c0-.6.4-1 1-1z"/></svg>+61491570156</li>
    <li><svg viewBox="0 0 10 10"><rect x="1" y="2" width="8" height="6"/></svg>delmo@vornikconsulting.com.au</li>
    <li><svg viewBox="0 0 10 10"><circle cx="5" cy="5" r="4"/></svg>www.vornikconsulting.com.au</li>
    <li><svg viewBox="0 0 10 10"><path d="M5 0a3.5 3.5 0 0 1 3.5 3.5C8.5 6 5 10 5 10S1.5 6 1.5 3.5A3.5 3.5 0 0 1 5 0z"/></svg>PO Box 417, Kelridge Heights, Tasmania, 7209</li>
  </ul>
</section>

<section class="sheet card logo-side">
  <div class="brand">Vornik Consulting</div>
  <div class="accent foot"></div>
  <div class="band foot"></div>
</section>

</body>
</html>
```